Heritage Hollow Business Cards

Require a business card design. <br/><br/>Needs to include logo (either round or long version) plus these details:<br/>Maya Torvel<br/>Heritage Hollow<br/>maya@quonbrook.com.au<br/>02 6481 7390<br/>PO Box Glenwarra NSW 2913<br/>www.heritagehollow.com.au<br/><br/>I need in an editable format so that I can create for multiple staff members. <br/><br/>

Target Market(s)

We are an online store selling renovation products to home owners are builders. Looking for a classic classy design.

Industry/Entity Type

Home And Garden

Contact Information for Business Card

Maya Torvel
Heritage Hollow
maya@quonbrook.com.au
02 6481 7390
PO Box Glenwarra NSW 2913
www.heritagehollow.com.au

Colors

Designer to choose colors to be used in the design.

Requirements
Must have
• Must include Logo.

```html
<!DOCTYPE html>
<html lang="en">
<head>
<meta charset="utf-8">
<title>Heritage Hollow Business Cards</title>
<link href="https://fonts.googleapis.com/css2?family=Roboto+Slab:wght@400;700&family=Work+Sans:wght@400&display=swap" rel="stylesheet">
<style>
  :root {
    --stage: #e4e2df;
    --ink: #1f1c1d;
    --ink-soft: #3a3536;
    --paper: #f5f6f7;
    --paper-text: #ffffff;
    --emboss: #3b3637;
  }
  * { margin: 0; padding: 0; box-sizing: border-box; }
  html, body { width: 1200px; height: 900px; overflow: hidden; background: var(--stage); }
  .sheet { position: relative; width: 1200px; height: 900px; display: flex; align-items: center; justify-content: center; gap: 40px; }
  .card { position: relative; width: 540px; height: 309px; overflow: hidden; }

  /* back */
  .card--back { background: var(--ink); }
  .back-mark { position: absolute; left: 50%; top: 50%; width: 190px; height: 190px; margin: -95px 0 0 -95px; border: 1.5px solid var(--emboss); border-radius: 50%; display: flex; align-items: center; justify-content: center; }
  .back-mark__name { font-family: "Roboto Slab", serif; font-weight: 400; font-size: 30px; line-height: 1.05; color: var(--emboss); text-align: center; }

  /* front */
  .card--front { background: var(--paper); }
  .front-brand { position: absolute; left: 300px; top: 28px; font-family: "Roboto Slab", serif; font-weight: 400; font-size: 34px; line-height: 1.02; color: var(--ink); }
  .holder { position: absolute; left: 30px; top: 150px; }
  .holder__name { font-family: "Roboto Slab", serif; font-weight: 700; font-size: 22px; letter-spacing: 2px; text-transform: uppercase; color: var(--ink); }
  .holder__company { font-family: "Work Sans", sans-serif; font-size: 12px; color: var(--ink-soft); margin-top: 1px; }
  .contact-band { position: absolute; left: 0; bottom: 0; width: 100%; height: 110px; background: var(--ink); }
  .contact { position: absolute; left: 30px; top: 213px; font-family: "Work Sans", sans-serif; font-size: 12px; line-height: 15px; color: var(--paper-text); list-style: none; }
  .contact li { display: flex; align-items: center; gap: 6px; }
  .contact li.address { display: block; padding-left: 0; margin-bottom: 2px; }
  .contact svg { width: 9px; height: 9px; flex: none; }
  .brand-seal { position: absolute; left: 375px; top: 140px; width: 230px; height: 230px; border-radius: 50%; border: 1.5px solid var(--ink); background: var(--paper); }
</style>
</head>
<body>
<main class="sheet">
  <section class="card card--back" aria-label="Card back">
    <div class="back-mark">
      <p class="back-mark__name">Heritage<br>Hollow</p>
    </div>
  </section>

  <section class="card card--front" aria-label="Card front">
    <p class="front-brand">Heritage<br>Hollow</p>
    <div class="holder">
      <h1 class="holder__name">Maya Torvel</h1>
      <p class="holder__company">Heritage Hollow</p>
    </div>
    <div class="contact-band"></div>
    <div class="brand-seal"></div>
    <ul class="contact">
      <li class="address">PO Box Glenwarra<br>NSW 2913</li>
      <li>
        <svg viewBox="0 0 10 10" aria-hidden="true"><path d="M2 0.8 L3.6 0.8 L4.2 3 L3.2 3.8 Q4.2 5.9 6.2 6.8 L7 5.8 L9.2 6.4 L9.2 8 Q9.2 9.2 8 9.2 Q1 8.6 0.8 2 Q0.8 0.8 2 0.8 Z" fill="#fff"/></svg>
        02 6481 7390
      </li>
      <li>
        <svg viewBox="0 0 10 10" aria-hidden="true"><rect x="0.7" y="2" width="8.6" height="6" fill="none" stroke="#fff" stroke-width="1"/><path d="M0.7 2 L5 5.4 L9.3 2" fill="none" stroke="#fff" stroke-width="1"/></svg>
        maya@quonbrook.com.au
      </li>
      <li>
        <svg viewBox="0 0 10 10" aria-hidden="true"><circle cx="5" cy="5" r="4.3" fill="none" stroke="#fff" stroke-width="0.9"/><ellipse cx="5" cy="5" rx="1.8" ry="4.3" fill="none" stroke="#fff" stroke-width="0.8"/><path d="M0.7 5 H9.3" stroke="#fff" stroke-width="0.8"/></svg>
        www.heritagehollow.com.au
      </li>
    </ul>
  </section>
</main>
</body>
</html>
```